Real Estate Web Design

Hi

We are a real estate agency who is looking for a Corporate Design that would match our Style Guide. We have already developed the website but we want to apply our Branding on top of it. I am looking for some creative concepts

Below is our Test link for our new website
http://brightnest.sampleview.com.au/

Attached is our Style Guide

Cheers
Tal

Industry/Entity Type

Real Estate

```html
<!DOCTYPE html>
<html lang="en">
<head>
<meta charset="utf-8">
<title>Brightnest Property Management</title>
<link rel="stylesheet" href="https://fonts.googleapis.com/css2?family=Arimo:wght@400;700&family=Roboto+Condensed:wght@300;400&display=swap">
<style>
:root{
  --navy:#0f2744;
  --nav:#16273d;
  --brand-blue:#0d4f9c;
  --red:#e8342c;
  --black:#0a0d12;
  --ink:#111;
  --white:#fff;
  --pale-blue:#8fa6d6;
  --sky-top:#2f6fc4;
  --sky-mid:#9cc3ea;
  --grass:#4d7a1f;
  --footer-grey:#d9d9db;
}
*{box-sizing:border-box;margin:0;padding:0}
html,body{width:1014px;height:1200px;overflow:hidden;background:var(--white)}
body{position:relative;font-family:Arimo,Helvetica,Arial,sans-serif;color:var(--ink)}
.abs{position:absolute}

/* header */
.topbar{left:0;top:0;width:1014px;height:32px;background:var(--navy);border-top:2px solid var(--red)}
.topbar .phone{position:absolute;right:34px;top:5px;color:var(--white);font:700 20px Arimo,Arial,sans-serif;letter-spacing:.5px}
.navbar{left:0;top:32px;width:1014px;height:39px;background:linear-gradient(#1c2e46,#101d2f)}
.nav{position:absolute;right:34px;top:12px;display:flex;list-style:none;font:400 11px "Roboto Condensed",Arial,sans-serif;color:var(--white);text-transform:uppercase}
.nav li+li::before{content:":";margin:0 15px}
.logo-block{left:54px;top:0;width:135px;height:110px;background:var(--brand-blue);border:2px solid #0a3b77;border-top:0;border-radius:0 0 6px 6px;z-index:5}
.logo-block .name{position:absolute;left:0;right:0;top:34px;text-align:center;color:var(--white);font:700 22px Arimo,Arial,sans-serif}
.logo-block .dot{position:absolute;left:59px;top:68px;width:16px;height:16px;border-radius:50%;background:var(--white)}

/* hero */
.hero{left:0;top:71px;width:1014px;height:419px;background:linear-gradient(180deg,var(--sky-top) 0%,var(--sky-mid) 45%,#cfe3f2 68%,#8bb64a 84%,var(--grass) 100%)}
.hero-photo{left:0;top:71px;width:620px;height:419px;background:radial-gradient(ellipse at 55% 55%,rgba(240,243,246,.75) 0%,rgba(240,243,246,.35) 35%,rgba(240,243,246,0) 60%)}
.headline{right:30px;top:84px;text-align:right;color:var(--white);font-family:"Roboto Condensed",Arial,sans-serif;font-weight:300}
.headline .l1{font-size:23px}
.headline .l2{font-size:37px;line-height:1.05}
.tagline{left:356px;top:232px;font:300 20px/24px "Roboto Condensed",Arial,sans-serif;color:#1b2430}
.tagline em{color:var(--red);font-style:italic}
.video{left:368px;top:337px;width:182px;height:96px;border:1px solid #6aa0e0;background:var(--white);padding:5px}
.video .screen{width:100%;height:100%;background:#777;position:relative}
.video svg{position:absolute;left:72px;top:27px}

/* search */
.search-head{left:613px;top:173px;width:401px;height:85px;background:var(--red);border-radius:6px 0 0 6px;color:var(--white);padding:12px 20px}
.search-head h2{font:300 25px "Roboto Condensed",Arial,sans-serif}
.search-head p{font-size:11px;line-height:13px;width:200px}
.search-head svg{position:absolute;left:242px;top:33px}
.search-panel{left:758px;top:258px;width:256px;height:232px;background:var(--red)}
.field{position:absolute;left:17px;width:222px;height:24px;background:var(--black);color:var(--white);font-size:11px;padding:6px 10px}
.field svg{position:absolute;right:8px;top:8px}
.search-btn{position:absolute;left:17px;top:186px;width:98px;height:24px;background:var(--navy);color:var(--white);font:700 9.5px/24px Arimo,Arial,sans-serif;text-align:center}
.circle-btn{width:46px;height:46px;border-radius:50%;background:var(--black);border:2px solid var(--white)}
.circle-btn svg{position:absolute;left:10px;top:12px}

/* services */
.services-top{left:0;top:490px;width:1014px;height:108px;background:linear-gradient(180deg,#3f6a1c,#26381a 70%,#1a2216)}
.services-bottom{left:0;top:598px;width:1014px;height:137px;background:var(--black)}
.service{position:absolute;top:514px;width:303px;color:var(--white)}
.service .thumb{position:absolute;left:0;top:10px;width:62px;height:62px;background:#000;border:1px solid #888}
.service h3{margin-left:73px;font:700 21px/25px Arimo,Arial,sans-serif}
.service .sub{position:absolute;left:73px;top:60px;font-size:12px}
.service .bar{position:absolute;left:0;top:84px;width:303px;height:5px}
.service .bar::after{content:"";position:absolute;left:20px;top:5px;border:12px solid transparent;border-top-color:inherit;border-bottom:0}
.service p{position:absolute;left:0;top:124px;font-size:15px;line-height:18px;width:300px}
.service .more{position:absolute;left:0;top:190px;font-size:15px;color:var(--pale-blue)}
.map{left:758px;top:605px;width:136px;height:126px;background:var(--pale-blue);border-radius:40% 45% 50% 40%}

/* testimonials */
.testimonials{left:0;top:735px;width:1014px;height:272px;background:linear-gradient(90deg,#fff 0%,#fff 35%,#e4e8ec 60%,#c9d3de 100%)}
.testimonials-title{left:28px;top:765px;font:300 52px "Roboto Condensed",Arial,sans-serif;color:var(--black)}
.quote-box{left:36px;top:840px;width:939px;height:138px;background:rgba(70,120,185,.72);border-radius:6px}
.quote-box svg{position:absolute;left:20px;top:14px}
.quote-box blockquote{position:absolute;left:96px;top:11px;width:820px;font-size:21px;line-height:25px;color:#0f1620}
.quote-box cite{position:absolute;left:96px;top:90px;font-style:normal;font-size:15px;line-height:18px;color:#0f1620}

/* footer */
.footer{left:0;top:1007px;width:1014px;height:193px;background:linear-gradient(#fff,var(--footer-grey));border-top:1px solid var(--brand-blue)}
.footer-bar{left:36px;top:1025px;width:939px;height:80px;background:var(--brand-blue);border-radius:6px;color:var(--white)}
.footer-logo{left:71px;top:1007px;width:134px;height:103px;background:var(--brand-blue);border:2px solid #0a3b77;border-radius:0 0 6px 6px;z-index:3}
.footer-logo .name{position:absolute;left:0;right:0;top:36px;text-align:center;color:var(--white);font:700 21px Arimo,Arial,sans-serif}
.address{left:221px;top:1039px;color:var(--white);font-size:12px;line-height:14px}
.footer-phone{left:221px;top:1072px;color:var(--white);font:700 20px Arimo,Arial,sans-serif}
.quick{color:var(--white);font-size:12px;writing-mode:vertical-rl;transform:rotate(180deg);height:72px;text-align:left;border-left:6px solid #0a3360;padding-left:2px}
.links{list-style:none;color:var(--white);font-size:11px;line-height:13.5px}
.social{width:21px;height:21px;border-radius:50%;background:#9cb6de}
.offer{left:0;width:1014px;top:1117px;text-align:center;font-size:22px;color:var(--brand-blue)}
.offer strong{color:var(--red)}
.legal{top:1167px;font-size:12px;color:var(--black)}
</style>
</head>
<body>

<header>
  <div class="abs topbar"><span class="phone">08 - 5550 - 1234</span></div>
  <nav class="abs navbar">
    <ul class="nav">
      <li>Home</li><li>About Us</li><li>Land Lords</li><li>Tenants</li><li>Properties</li><li>Contact Us</li><li>Franchise Opportunities</li><li>Testimonials</li>
    </ul>
  </nav>
  <div class="abs logo-block"><span class="name">brightnest</span><span class="dot"></span></div>
</header>

<section>
  <div class="abs hero" role="img" aria-label="Hand holding a paper house cut-out against blue sky and green grass"></div>
  <div class="abs hero-photo"></div>
  <div class="abs headline">
    <div class="l1">for the best people to manage and care for your property investment,</div>
    <div class="l2">there is no alternative</div>
  </div>
  <div class="abs tagline">Land Lords<br>Tenants<br><em>Simply what you need</em></div>
  <div class="abs video"><div class="screen">
    <svg width="26" height="26" viewBox="0 0 26 26"><circle cx="13" cy="13" r="13" fill="#555"/><path d="M11 7l6 6-6 6" fill="none" stroke="#fff" stroke-width="2"/></svg>
  </div></div>

  <div class="abs search-head">
    <h2>Property Search</h2>
    <p>Brightnest Property Management is your first choice for everything to do with renting</p>
    <svg width="36" height="20" viewBox="0 0 36 20"><path d="M2 2l16 14L34 2" fill="none" stroke="#fff" stroke-width="4"/></svg>
  </div>
  <div class="abs search-panel">
    <div class="field" style="top:12px">property type<svg width="14" height="8" viewBox="0 0 14 8"><path d="M1 1l6 5 6-5" fill="none" stroke="#fff" stroke-width="2"/></svg></div>
    <div class="field" style="top:39px">suburb<svg width="14" height="8" viewBox="0 0 14 8"><path d="M1 1l6 5 6-5" fill="none" stroke="#fff" stroke-width="2"/></svg></div>
    <div class="field" style="top:66px">price from<svg width="14" height="8" viewBox="0 0 14 8"><path d="M1 1l6 5 6-5" fill="none" stroke="#fff" stroke-width="2"/></svg></div>
    <div class="field" style="top:93px">price to<svg width="14" height="8" viewBox="0 0 14 8"><path d="M1 1l6 5 6-5" fill="none" stroke="#fff" stroke-width="2"/></svg></div>
    <div class="field" style="top:120px">bedrooms<svg width="14" height="8" viewBox="0 0 14 8"><path d="M1 1l6 5 6-5" fill="none" stroke="#fff" stroke-width="2"/></svg></div>
    <div class="field" style="top:147px">pets considered<svg width="14" height="8" viewBox="0 0 14 8"><path d="M1 1l6 5 6-5" fill="none" stroke="#fff" stroke-width="2"/></svg></div>
    <div class="search-btn">Search Properties</div>
  </div>
</section>

<section>
  <div class="abs services-top" role="img" aria-label="Close-up of green grass"></div>
  <div class="abs services-bottom"></div>
  <div class="abs circle-btn" style="left:497px;top:466px;z-index:4">
    <svg width="24" height="18" viewBox="0 0 24 18"><path d="M2 4l10 10L22 4" fill="none" stroke="#fff" stroke-width="4"/></svg>
  </div>

  <div class="service" style="left:27px">
    <div class="thumb"></div>
    <h3>Do you want your property managed?</h3>
    <span class="sub">Luxury End Appartments</span>
    <div class="bar" style="background:var(--red);border-color:var(--red)"></div>
    <p>For the past 10 years in the South West we have been the leading specialist rental company.</p>
    <span class="more">Know more...</span>
  </div>
  <div class="service" style="left:360px">
    <div class="thumb"></div>
    <h3>How much rent can I get per week?</h3>
    <span class="sub">Luxury End Appartments</span>
    <div class="bar" style="background:var(--brand-blue);border-color:var(--brand-blue)"></div>
    <p>For the past 10 years in the South West we have been the leading specialist rental company.</p>
    <span class="more">Know more...</span>
  </div>
  <div class="service" style="left:693px">
    <div class="thumb"></div>
    <h3>Franchise opportunities</h3>
    <span class="sub">Luxury End Appartments</span>
    <div class="bar" style="background:var(--pale-blue);border-color:var(--pale-blue)"></div>
  </div>
  <div class="abs map" role="img" aria-label="Map of Australia with state borders"></div>
</section>

<section>
  <div class="abs testimonials" role="img" aria-label="Couple looking up at a white two-storey house"></div>
  <h2 class="abs testimonials-title">What our customers think</h2>
  <div class="abs quote-box">
    <svg width="64" height="40" viewBox="0 0 64 40"><path d="M4 38c-4-14 2-30 18-36l2 5c-8 4-10 9-9 13 5 0 9 4 9 9s-4 9-10 9c-4 0-8-1-10 0zM36 38c-4-14 2-30 18-36l2 5c-8 4-10 9-9 13 5 0 9 4 9 9s-4 9-10 9c-4 0-8-1-10 0z" fill="var(--red)"/></svg>
    <blockquote>My wife and I have been with this company for over 10 years now and have found the service to be at a very professional standard....</blockquote>
    <cite>Daniel Reeve<br>Coral Bay</cite>
  </div>
  <div class="abs circle-btn" style="left:480px;top:975px;z-index:4">
    <svg width="24" height="18" viewBox="0 0 24 18"><path d="M2 14L12 4l10 10" fill="none" stroke="#fff" stroke-width="4"/></svg>
  </div>
</section>

<footer>
  <div class="abs footer"></div>
  <div class="abs footer-bar"></div>
  <div class="abs footer-logo"><span class="name">brightnest</span></div>
  <div class="abs address">First Floor 42 Harbour Street<br>Coral Bay WA 6701</div>
  <div class="abs footer-phone">08 - 5550 - 1234</div>
  <div class="abs quick" style="left:449px;top:1030px">Quick Links</div>
  <ul class="abs links" style="left:483px;top:1033px">
    <li>Frequently asked Questions</li><li>How do i pay rent?</li><li>Tenant Policies</li><li>Tenants Information</li>
  </ul>
  <div class="abs quick" style="left:668px;top:1030px">Quick Links</div>
  <ul class="abs links" style="left:702px;top:1033px">
    <li>Newsletter</li><li>Legal Information</li><li>Siemap</li>
  </ul>
  <div class="abs social" style="left:883px;top:1041px"></div>
  <div class="abs social" style="left:910px;top:1041px"></div>
  <p class="abs offer">Contact us today and ask about our 60 day <strong>Free Management offer!</strong></p>
  <span class="abs legal" style="left:346px">©2013 Brightnest Property Management</span>
  <span class="abs legal" style="left:578px">Terms &amp; Privacy</span>
</footer>

</body>
</html>
```